依頼詳細
「ほがらか酵素」のパッケージデザインをアルミ袋デザインを依頼させて頂きます。「安心」「安全」「清潔感」をパッケージから感じることができ、ターゲットである「35歳、女性、未婚、バリバリ働く女性でも婚活中」がバックの中に入れて常に持ち運び、人前で袋を取り出しても恥ずかしくない、おしゃれな(カッコいい)デザインを希望します。
「ほがらか酵素」は、体質改善、花粉症、便秘、肥満、冷え性、睡眠改善、肌荒れ、胃もたれ、白髪など、あらゆるお悩みに対して効果が期待できます。
コラーゲン、ヒアルロン酸、グルコサミンなどあらゆる健康食品を摂取する前に摂取して頂きたいサプリメントです。
記載項目
<アルミ平袋>
サイズ:W100mm×H145mm(チャック上20㎜チャック下125㎜)
印刷/カラー:デジタル印刷
基材:PE(透明)
希望イメージ
シンプル 複雑
単色 カラフル
暗い 明るい
日常 高級
遊び心 厳粛
未来的 伝統的
女性的 男性的
希望する色
明るい色
納品ファイル
• 高解像度JPG (.jpg)
• イラストレーター形式 (.ai)
補足説明
可能であれば、パッケージに会社のロゴマークを入れたいと考えております。(添付ファイルをご確認下さい。)
添付書類がなかったようなので、添付させて頂きます。
ほがらか酵素は、野菜や果物は使っていませんので、野菜や果物のイメージがあるデザインは使えないので、ご考慮お願い致します。
■ 選んだ理由

イメージしていた内容そのままで、女性の支持が多かったので選定させて頂きました。

■ 提案者全員のお礼・コメント

たくさんのご提案ありがとうございました。

```html
<!DOCTYPE html>
<html lang="ja">
<head>
<meta charset="utf-8">
<title>ほがらか酵素 パッケージ</title>
<link href="https://fonts.googleapis.com/css2?family=Cinzel:wght@400;500&family=Shippori+Mincho:wght@600;800&display=swap" rel="stylesheet">
<style>
  :root {
    --page: #ffffff;
    --gold-dark: #b8925a;
    --gold-light: #f3e2bd;
    --green-top: #9fcf6e;
    --green-mid: #c3e19d;
    --green-pale: #e6f2d4;
    --cream: #fffdf6;
    --title-green: #2f6a1f;
    --body-brown: #4a3520;
    --accent-orange: #e8891e;
  }
  * { margin: 0; padding: 0; box-sizing: border-box; }
  html, body { width: 848px; height: 1200px; overflow: hidden; background: var(--page); }
  .canvas { position: relative; width: 848px; height: 1200px; }
  .pouch {
    position: absolute; left: 192px; top: 71px; width: 464px; height: 671px;
    overflow: hidden;
    background: linear-gradient(180deg, var(--page) 0 34px, var(--green-top) 70px, var(--green-mid) 260px, var(--green-pale) 440px, var(--cream) 560px);
  }
  .gold-band {
    position: absolute; left: 0; width: 100%;
    background: linear-gradient(90deg, var(--gold-dark), var(--gold-light) 45%, var(--gold-dark));
  }
  .gold-band--top { top: 34px; height: 36px; }
  .gold-band--bottom { bottom: 0; height: 22px; }
  .lower-sweep { position: absolute; left: 0; top: 450px; width: 464px; height: 200px; }
  .leaf-art {
    position: absolute; left: 142px; top: 121px; width: 153px; height: 153px; border-radius: 50%;
    background: radial-gradient(circle, rgba(255,255,255,0.75), rgba(255,255,255,0.15) 70%, transparent);
  }
  .brand-latin {
    position: absolute; left: 0; width: 100%; text-align: center;
    font-family: "Cinzel", serif; color: #ffffff; font-weight: 500;
  }
  .brand-latin--small { top: 282px; font-size: 34px; letter-spacing: 3px; }
  .brand-latin--large { top: 318px; font-size: 60px; letter-spacing: 5px; }
  .product-name {
    position: absolute; left: 0; top: 394px; width: 100%; text-align: center;
    font-family: "Shippori Mincho", serif; font-weight: 800; font-size: 47px;
    color: var(--title-green); letter-spacing: 1px;
  }
  .description {
    position: absolute; left: 0; top: 509px; width: 100%; text-align: center;
    font-family: "Shippori Mincho", serif; font-weight: 800; font-size: 18px;
    line-height: 24px; color: var(--body-brown);
  }
  .maker {
    position: absolute; left: 0; top: 582px; width: 100%;
    display: flex; justify-content: center; align-items: center; gap: 6px;
    font-family: "Shippori Mincho", serif; font-weight: 600; font-size: 14px; color: var(--accent-orange);
  }
  .maker__dot { width: 22px; height: 22px; border-radius: 50%; background: var(--accent-orange); }
  .count {
    position: absolute; right: 22px; top: 618px;
    font-family: "Shippori Mincho", serif; font-weight: 600; font-size: 16px; color: var(--body-brown);
  }
</style>
</head>
<body>
<div class="canvas">
  <div class="pouch">
    <div class="gold-band gold-band--top"></div>
    <svg class="lower-sweep" viewBox="0 0 464 200" aria-hidden="true">
      <path d="M0 40 Q232 -10 464 30 L464 200 L0 200 Z" fill="#fffdf6"/>
    </svg>
    <div class="leaf-art" role="img" aria-label="白い葉と新芽の装飾イラスト"></div>
    <div class="brand-latin brand-latin--small">HOGARAKA</div>
    <div class="brand-latin brand-latin--large">ENZYME</div>
    <div class="product-name">ほがらか酵素</div>
    <p class="description">麹菌を大豆や小麦などの穀物で<br>発酵させた酵素が<br>あなたの元気を応援します。</p>
    <div class="maker"><span class="maker__dot"></span><span>ひなた堂</span></div>
    <div class="count">30粒</div>
    <div class="gold-band gold-band--bottom"></div>
  </div>
</div>
</body>
</html>
```